Velmar Intergrated Marketing Stationary Design Contest

We require a very professional looking stationary set to include: letterhead, compliments slip and business cards (double sided bus cards).

Files should be supplied on either Illustrator or InDesign.

We are interested in perhaps encorporating a faint watermark with the letter q or the logo, but it isnt a pre-requisite

Target Market(s)

Business owners seeking professional marketing services

Industry/Entity Type

Marketing

Requirements
Must have
• Concurrent theme wiht business cards, letterhead and comp slip. Must be an editable document for future ammendment
Should not have
• No use of times new roman or similar fonts

```html
<!DOCTYPE html>
<html lang="en">
<head>
<meta charset="utf-8">
<title>Velmar Intergrated Marketing – Business Card</title>
<link href="https://fonts.googleapis.com/css2?family=Figtree:wght@300;400;600&display=swap" rel="stylesheet">
<style>
  :root {
    --card-orange: #ed7b44;
    --swirl-orange: #e9582f;
    --swirl-light: #ee8450;
    --text-white: #ffffff;
    --text-blush: #f8d2c3;
    --divider: #1c1c1c;
  }
  html, body {
    margin: 0;
    padding: 0;
    overflow: hidden;
    background: var(--card-orange);
  }
  .card {
    position: relative;
    width: 1200px;
    height: 600px;
    overflow: hidden;
    background: var(--card-orange);
    font-family: "Figtree", "Helvetica Neue", Arial, sans-serif;
    color: var(--text-white);
  }
  .card__decoration {
    position: absolute;
    inset: 0;
  }
  .card__column {
    position: absolute;
    top: 0;
    height: 600px;
  }
  .card__column--company { left: 44px; width: 540px; }
  .card__column--person { left: 656px; width: 520px; }
  .headline {
    position: absolute;
    top: 100px;
    margin: 0;
    font-weight: 300;
    font-size: 44px;
    line-height: 1;
    white-space: nowrap;
  }
  .headline--company {
    top: 102px;
    font-size: 41px;
    letter-spacing: -0.2px;
  }
  .subline {
    position: absolute;
    top: 168px;
    margin: 0;
    font-weight: 400;
    font-size: 29px;
    line-height: 1;
    white-space: nowrap;
  }
  .subline--title { color: var(--text-blush); }
  .detail-list {
    position: absolute;
    top: 400px;
    margin: 0;
    padding: 0;
    list-style: none;
    font-weight: 300;
    font-size: 29px;
    line-height: 42.5px;
    white-space: nowrap;
  }
  .detail-list__label {
    display: inline-block;
    width: 46px;
    font-weight: 600;
    color: var(--text-blush);
  }
  .divider {
    position: absolute;
    left: 600px;
    top: 0;
  }
</style>
</head>
<body>
  <div class="card">
    <svg class="card__decoration" width="1200" height="600" viewBox="0 0 1200 600" role="img" aria-label="Abstract swirling orb decoration in deep orange">
      <defs>
        <radialGradient id="orbGradient" cx="50%" cy="40%" r="60%">
          <stop offset="0%" stop-color="#ea5b31"/>
          <stop offset="85%" stop-color="#e9582f"/>
          <stop offset="100%" stop-color="#eb6a3a"/>
        </radialGradient>
      </defs>
      <ellipse cx="615" cy="190" rx="525" ry="380" fill="url(#orbGradient)"/>
    </svg>

    <svg class="divider" width="4" height="600" viewBox="0 0 4 600" aria-hidden="true">
      <g stroke="var(--divider)" stroke-width="2">
        <line x1="2" y1="42" x2="2" y2="90"/>
        <line x1="2" y1="139" x2="2" y2="187"/>
        <line x1="2" y1="236" x2="2" y2="284"/>
        <line x1="2" y1="333" x2="2" y2="381"/>
        <line x1="2" y1="430" x2="2" y2="478"/>
        <line x1="2" y1="527" x2="2" y2="575"/>
      </g>
    </svg>

    <section class="card__column card__column--company">
      <h1 class="headline headline--company">Velmar Intergrated Marketing</h1>
      <p class="subline">Tag line can go here</p>
      <ul class="detail-list">
        <li>Kestrel House</li>
        <li>Mill Lane</li>
        <li>Ashworth</li>
        <li>West Yorkshire WF99 4QT</li>
      </ul>
    </section>

    <section class="card__column card__column--person">
      <h2 class="headline">Martin Holloway</h2>
      <p class="subline subline--title">General Manager</p>
      <ul class="detail-list">
        <li><span class="detail-list__label">t</span>01632 960514</li>
        <li><span class="detail-list__label">f</span>01632 960511</li>
        <li><span class="detail-list__label">e</span>martin@velmarim.co.uk</li>
        <li><span class="detail-list__label">w</span>www.velmarim.co.uk</li>
      </ul>
    </section>
  </div>
</body>
</html>
```